Peter Lasko-Wren Finance

Need a personal website advertising Equipment Finance,Business Finance,Commercial Finance, Construction Finance, Bridging Finance. Similar websites are www.varoplend.com.au / www.kitmoxa.com.au / www.rzb4.com.au /wwwbelvaxcredit.com.au

Target Market(s)

Business People

Industry/Entity Type

Business

Number of Pages Required

3 page

Font styles to use
Serif
Sans Serif

Requirements
Must have
• All i want is a simple corporate looking website advertising Equipment Finance, Commercial Finance, Construction Finance, Business Finance, Bridging Finance,

```html
<!DOCTYPE html>
<html lang="en">
<head>
<meta charset="utf-8">
<title>Peter Lasko-Wren Finance</title>
<link href="https://fonts.googleapis.com/css2?family=Open+Sans:wght@400;600;700&family=Roboto:wght@300;400;700&display=swap" rel="stylesheet">
<style>
:root{
  --navy:#0d2d55;
  --blue:#00a8ec;
  --pale:#eef6fd;
  --grey:#e1e6ea;
  --text:#555;
  --light:#9a9a9a;
  --white:#fff;
}
*{margin:0;padding:0;box-sizing:border-box}
html,body{width:702px;height:1200px;overflow:hidden}
body{position:relative;background:var(--white);font-family:"Open Sans",Arial,sans-serif;color:var(--text)}
.abs{position:absolute}
.topbar{left:0;top:0;width:702px;height:23px;background:var(--pale);border-bottom:1px solid #dde6ef}
.top-contact{left:94px;top:0;height:23px;width:44px;font-size:6.5px;font-weight:600;color:var(--navy);line-height:23px;text-align:center;border-left:1px solid #d6e0ea;border-right:1px solid #d6e0ea;white-space:nowrap}
.social-sq{top:5px;width:12px;height:12px;border:1.5px solid var(--navy);border-radius:2px}
.quick-tab{left:544px;top:4px;width:70px;height:19px;background:var(--navy);color:var(--white);font-size:6.5px;font-weight:600;text-align:center;line-height:19px;clip-path:polygon(6% 0,94% 0,100% 100%,0 100%)}
.brand{left:89px;top:34px;width:92px}
.brand .name{font-size:10px;font-weight:700;color:var(--navy);line-height:12px;white-space:nowrap}
.brand .sub{font-size:7.5px;font-weight:400;color:var(--navy);text-align:right;border-top:1px solid var(--navy);margin-top:2px;padding-top:1px;line-height:9px}
.mainnav{left:195px;top:42px;display:flex;gap:13px;font-size:6.5px;color:var(--navy)}
.mainnav .active{border-bottom:1.5px solid var(--blue);padding-bottom:3px}
.phone{left:530px;top:35px;font-family:Roboto,sans-serif;font-size:14px;color:var(--navy)}
.servicebar{left:0;top:69px;width:702px;height:20px;background:var(--blue);display:flex;padding-left:89px;font-size:7px;color:var(--white);line-height:20px}
.servicebar span{margin-right:20px}
.hero{left:0;top:89px;width:702px;height:221px;background:linear-gradient(90deg,#9dbad3 0%,#d9e6f1 35%,#e8eff5 60%,#c9d8e4 100%)}
.hero-person{left:502px;top:89px;width:200px;height:221px;background:linear-gradient(180deg,#cfb9a6 0%,#2a2f3a 45%,#1b1f28 100%)}
.hero-title{left:95px;top:141px;font-family:Roboto,sans-serif;font-weight:700;font-size:21px;line-height:24px;color:var(--navy);white-space:nowrap}
.hero-sub{left:95px;top:170px;width:300px;font-family:Roboto,sans-serif;font-weight:300;font-size:12.5px;line-height:16px;color:var(--navy)}
.btn-quote{left:99px;top:219px;width:88px;height:22px;background:var(--navy);color:var(--white);font-size:7px;font-weight:600;display:flex;align-items:center;justify-content:center;gap:5px}
.partners{left:100px;top:322px;width:500px;height:24px;display:flex;justify-content:space-between;align-items:center}
.badge{height:12px;background:#b7c4d2;border-radius:2px}
.rule{left:89px;top:359px;width:526px;height:1px;background:#ccd3da}
.welcome{left:0;top:374px;width:702px;text-align:center;font-family:Roboto,sans-serif;font-weight:300;font-size:21px;color:var(--navy)}
.welcome-text{left:100px;top:420px;width:502px;text-align:center;font-size:6.3px;line-height:8.3px;color:#444}
.band{left:0;top:480px;width:702px;height:320px;background:var(--pale)}
.card{width:175px;height:112px;background:var(--white);text-align:center;padding-top:10px}
.card svg{display:block;margin:0 auto}
.card h3{font-size:8px;font-weight:400;color:#222;margin-top:6px}
.card .bar{width:40px;height:1px;background:var(--blue);margin:5px auto 6px}
.card p{font-size:6px;line-height:7.3px;color:var(--light);padding:0 28px}
.callout{left:441px;top:640px;width:174px;height:112px;background:var(--blue);color:var(--white);text-align:center;padding-top:15px}
.callout .lbl{font-size:7.5px}
.callout .num{font-size:13px;margin-top:6px}
.callout p{font-size:6px;line-height:7.5px;font-weight:600;margin-top:5px;padding:0 30px}
.callout .btn{width:84px;height:19px;background:var(--navy);margin:7px auto 0;font-size:6.5px;line-height:19px;font-weight:600}
.photo{top:832px;width:174px;height:130px}
.post{top:968px;width:174px;text-align:center}
.post h4{font-size:8.5px;font-weight:400;color:#222}
.post .bar{width:40px;height:1px;background:var(--blue);margin:5px auto 5px}
.post p{font-size:6px;line-height:7.3px;color:var(--light);padding:0 12px}
.post a{display:block;font-size:6.5px;color:var(--blue);margin-top:4px;text-decoration:none}
.footer{left:0;top:1051px;width:702px;height:110px;background:var(--grey)}
.flinks{font-size:6.2px;color:var(--navy);line-height:13.2px}
.sub-title{left:357px;top:1079px;font-size:6.5px;color:#222}
.email{left:357px;top:1093px;width:148px;height:20px;background:var(--white);font-size:6px;color:#888;padding-left:6px;line-height:20px}
.subscribe{left:515px;top:1093px;width:84px;height:20px;background:var(--blue);color:var(--white);font-size:8px;text-align:center;line-height:20px}
.dot{top:1120px;width:13px;height:13px;border-radius:50%;background:var(--navy)}
.copy{left:0;top:1178px;width:702px;text-align:center;font-size:5.5px;color:#222}
</style>
</head>
<body>
<header>
  <div class="abs topbar"></div>
  <div class="abs top-contact">Contact Us</div>
  <div class="abs social-sq" style="left:143px"></div>
  <div class="abs social-sq" style="left:165px"></div>
  <div class="abs social-sq" style="left:187px"></div>
  <div class="abs social-sq" style="left:209px"></div>
  <div class="abs quick-tab">QUICK QUOTE</div>

  <div class="abs brand"><div class="name">Peter Lasko-Wren</div><div class="sub">Finance</div></div>
  <nav class="abs mainnav"><span class="active">HOME</span><span>ABOUT PETER</span><span>CONTACT</span></nav>
  <div class="abs phone">555-014-2290</div>

  <nav class="abs servicebar"><span>Equipment Finance</span><span>Commercial Finance</span><span>Construction Finance</span><span>Business Finance</span><span>Bridging Finance</span></nav>
</header>

<section>
  <div class="abs hero" role="img" aria-label="Blurred office building and business people in the background"></div>
  <div class="abs hero-person" role="img" aria-label="Businessman in a suit offering a handshake"></div>
  <h1 class="abs hero-title">FINANCE SOLUTIONS</h1>
  <div class="abs hero-sub">LOREM IPSUM DOLOR SIT AMET, CONSECTETUR ADIPISCING ELIT. SED EUISMOD ODIO</div>
  <div class="abs btn-quote">
    <svg width="11" height="6" viewBox="0 0 11 6"><path d="M0 3H10M7 0.5L10 3L7 5.5" stroke="#fff" fill="none" stroke-width="1"/></svg>GET QUOTE
  </div>
</section>

<section class="abs partners" aria-label="Lending partners">
  <div class="badge" style="width:38px"></div>
  <div class="badge" style="width:62px"></div>
  <div class="badge" style="width:60px"></div>
  <div class="badge" style="width:48px"></div>
  <div class="badge" style="width:58px"></div>
  <div class="badge" style="width:63px;height:22px;background:#e21f26"></div>
  <div class="badge" style="width:46px"></div>
</section>
<div class="abs rule"></div>

<section>
  <h2 class="abs welcome">Welcome</h2>
  <p class="abs welcome-text">Lorem ipsum dolor sit amet, consectetur adipiscing elit. Sed vel semper risus, id consequat mauris. Curabitur sit amet accumsan est, at sollicitudin nunc. Nullam semper at nulla eget dictum. Fusce mollis laoreet mattis. Suspendisse eget sagittis dolor. Phasellus facilisis quam dolor. Donec ac odio et justo ultricies efficitur at pharetra sem. Sed blandit, velit in tristique volutpat, libero mi pellentesque dolor, sed porta eros lacus ut odio. Etiam tempus ipsum justo, eget faucibus augue dignissim ac. Phasellus sit amet vulputate felis. Proin ligula ante, porta id posuere in, finibus sit amet mauris.</p>
</section>

<section>
  <div class="abs band"></div>
  <div class="abs card" style="left:89px;top:527px">
    <svg width="30" height="28" viewBox="0 0 30 28"><rect x="4" y="10" width="14" height="11" fill="none" stroke="#00a8ec" stroke-width="2"/><rect x="8" y="4" width="7" height="6" fill="none" stroke="#0d2d55" stroke-width="1.5"/><path d="M21 2V24H29" stroke="#00a8ec" stroke-width="2" fill="none"/><circle cx="8" cy="23" r="3" fill="#0d2d55"/><circle cx="16" cy="23" r="3" fill="#0d2d55"/></svg>
    <h3>Equipment Finance</h3><div class="bar"></div>
    <p>Lorem ipsum dolor sit amet, consectetur adipiscing elit. Sed euismod odio vitae orci tempor, eget egestas nunc condimentum.</p>
  </div>
  <div class="abs card" style="left:265px;top:527px">
    <svg width="30" height="28" viewBox="0 0 30 28"><rect x="3" y="17" width="4" height="9" fill="#00a8ec"/><rect x="10" y="12" width="4" height="14" fill="#00a8ec"/><rect x="17" y="14" width="4" height="12" fill="#00a8ec"/><rect x="24" y="8" width="4" height="18" fill="#00a8ec"/><path d="M3 13L11 6L18 10L27 2" stroke="#0d2d55" stroke-width="1.5" fill="none"/></svg>
    <h3>Commercial Finance</h3><div class="bar"></div>
    <p>Lorem ipsum dolor sit amet, consectetur adipiscing elit. Sed euismod odio vitae orci tempor, eget egestas nunc condimentum.</p>
  </div>
  <div class="abs card" style="left:441px;top:527px">
    <svg width="30" height="26" viewBox="0 0 30 26"><rect x="7" y="2" width="16" height="23" fill="none" stroke="#00a8ec" stroke-width="2"/><rect x="11" y="6" width="3" height="3" fill="#0d2d55"/><rect x="16" y="6" width="3" height="3" fill="#0d2d55"/><rect x="11" y="12" width="3" height="3" fill="#0d2d55"/><rect x="16" y="12" width="3" height="3" fill="#0d2d55"/><rect x="13" y="18" width="4" height="7" fill="#0d2d55"/></svg>
    <h3>Construction Finance</h3><div class="bar"></div>
    <p>Lorem ipsum dolor sit amet, consectetur adipiscing elit. Sed euismod odio vitae orci tempor, eget egestas nunc condimentum.</p>
  </div>
  <div class="abs card" style="left:89px;top:640px">
    <svg width="30" height="28" viewBox="0 0 30 28"><path d="M2 8L9 5L15 9L21 5L28 8L26 18L18 24L12 20L4 17Z" fill="#00a8ec"/><path d="M9 13L14 17M12 11L17 15" stroke="#fff" stroke-width="1.2"/></svg>
    <h3>Business Finance</h3><div class="bar"></div>
    <p>Lorem ipsum dolor sit amet, consectetur adipiscing elit. Sed euismod odio vitae orci tempor, eget egestas nunc condimentum.</p>
  </div>
  <div class="abs card" style="left:265px;top:640px">
    <svg width="32" height="28" viewBox="0 0 32 28"><rect x="2" y="4" width="20" height="18" fill="none" stroke="#00a8ec" stroke-width="2"/><rect x="2" y="4" width="20" height="4" fill="#00a8ec"/><path d="M7 12H9M12 12H14M17 12H19M7 16H9M12 16H14" stroke="#0d2d55" stroke-width="1.5"/><rect x="17" y="16" width="13" height="8" fill="#fff" stroke="#00a8ec" stroke-width="1.5"/><circle cx="23.5" cy="20" r="2" fill="none" stroke="#0d2d55"/></svg>
    <h3>Bridging Finance</h3><div class="bar"></div>
    <p>Lorem ipsum dolor sit amet, consectetur adipiscing elit. Sed euismod odio vitae orci tempor, eget egestas nunc condimentum.</p>
  </div>
  <div class="abs callout">
    <div class="lbl">For More Info Call:</div>
    <div class="num">555-014-2290</div>
    <p>Lorem ipsum dolor sit amet, consectetur adipiscing elit.</p>
    <div class="btn">QUICK QUOTE</div>
  </div>
</section>

<section>
  <div class="abs photo" style="left:89px;background:linear-gradient(135deg,#e8e8e8,#c9c9c9)" role="img" aria-label="Person in a hoodie working on a laptop"></div>
  <div class="abs photo" style="left:265px;background:linear-gradient(135deg,#a58a6a,#6f7b8c 55%,#dfe3ea)" role="img" aria-label="Colleagues reviewing documents around a laptop on a desk"></div>
  <div class="abs photo" style="left:441px;background:linear-gradient(135deg,#f0f0f0,#cfd4da)" role="img" aria-label="Customer service team wearing headsets"></div>

  <div class="abs post" style="left:89px"><h4>In aliquam tortor et nunc maximus</h4><div class="bar"></div><p>Lorem ipsum dolor sit amet, consectetur adipiscing elit. Sed euismod odio vitae orci tempor, eget egestas nunc condimentum.</p><a href="#">- Read more</a></div>
  <div class="abs post" style="left:265px"><h4>In aliquam tortor et nunc maximus</h4><div class="bar"></div><p>Lorem ipsum dolor sit amet, consectetur adipiscing elit. Sed euismod odio vitae orci tempor, eget egestas nunc condimentum.</p><a href="#">- Read more</a></div>
  <div class="abs post" style="left:441px"><h4>In aliquam tortor et nunc maximus</h4><div class="bar"></div><p>Lorem ipsum dolor sit amet, consectetur adipiscing elit. Sed euismod odio vitae orci tempor, eget egestas nunc condimentum.</p><a href="#">- Read more</a></div>
</section>

<footer>
  <div class="abs footer"></div>
  <div class="abs flinks" style="left:100px;top:1074px">EQUIPMENT FINANCE<br>COMMERCIAL FINANCE<br>CONSTRUCTION FINANCE<br>BUSINESS FINANCE<br>BRIDGING FINANCE</div>
  <div class="abs flinks" style="left:254px;top:1075px">HOME<br>ABOUT PETER<br>CONTACT</div>
  <div class="abs sub-title">SUBSCRIBE FOR THE LATEST NEWS</div>
  <div class="abs email">Enter Your Email</div>
  <div class="abs subscribe">SUBSCRIBE</div>
  <div class="abs dot" style="left:357px"></div>
  <div class="abs dot" style="left:375px"></div>
  <div class="abs dot" style="left:393px"></div>
  <div class="abs dot" style="left:411px"></div>
  <div class="abs copy">Copyright 2017 laskowrenfinance.com All Rights Reserved.</div>
</footer>
</body>
</html>
```